Business Card Design Project

Build kick ass business card.
Updates

I just uploaded the Veruxo Logo in AI format, for those that were asking. It's looking real good and we'll be reviewing the designs soon. Thanks. 

Target Market(s)

Businesses in many verticals. Focusing on information security.

Veruxo, LLC
Darren Colby
Principal Security Consultant
Mobile: +1-480-555-0137
Email: Darren.Colby@Veruxo.example
Web: www.veruxo.example

Industry/Entity Type

Business

Requirements
Must have
• Design must look high-end, hi-tech stylish and minimalist

Be different – one that stands out from thousands of others

Does not have to be traditional rectangle

Would like logo integrated

```html
<!DOCTYPE html>
<html lang="en">
<head>
<meta charset="utf-8">
<title>Veruxo Business Card</title>
<link href="https://fonts.googleapis.com/css2?family=Ubuntu:wght@300;400&display=swap" rel="stylesheet">
<style>
  :root{
    --backdrop:#ececec;
    --card:#f7f7f7;
    --card-edge:#d8d8d8;
    --clear-plastic:#e4e6e8;
    --walnut:#5a2e12;
    --walnut-dark:#3e1e0a;
    --ink:#1f1f1f;
    --ink-soft:#444;
    --accent:#1f8fcf;
    --rule:#bdbdbd;
  }
  *{box-sizing:border-box;margin:0;padding:0}
  html,body{width:1200px;height:675px;overflow:hidden}
  body{background:var(--backdrop);font-family:"Ubuntu",sans-serif;color:var(--ink);position:relative}

  .brand{display:flex;align-items:center;gap:10px}
  .brand-dot{border-radius:50%;background:var(--accent);flex:none}
  .brand-text{display:flex;flex-direction:column}
  .brand-name{font-weight:400;color:var(--ink);letter-spacing:.02em;line-height:1}
  .brand-tagline{font-weight:300;color:var(--ink-soft);letter-spacing:.08em;margin-top:4px}

  .hero-brand{position:absolute;left:760px;top:80px}
  .hero-brand .brand-dot{width:90px;height:90px}
  .hero-brand .brand-name{font-size:50px}
  .hero-brand .brand-tagline{font-size:17px}

  .card{position:absolute;background:var(--clear-plastic);border-radius:20px;overflow:hidden;
        box-shadow:0 6px 14px rgba(0,0,0,.25);border:1px solid var(--card-edge)}

  /* Vertical card */
  .card-vertical{left:352px;top:169px;width:253px;height:434px}
  .card-vertical .head{position:absolute;left:0;top:0;width:100%;height:131px;background:var(--card)}
  .card-vertical .head .brand{position:absolute;left:16px;top:42px}
  .card-vertical .band{position:absolute;left:0;top:131px;width:205px;height:303px;
        background:var(--walnut);border-top-right-radius:16px}
  .card-vertical .panel{position:absolute;left:0;top:154px;width:187px;height:280px;
        background:var(--card);border-top-right-radius:14px}
  .card-small .brand-dot{width:40px;height:40px}
  .card-small .brand-name{font-size:26px}
  .card-small .brand-tagline{font-size:9.5px}

  .identity{position:absolute;left:0;top:36px;width:100%;text-align:center}
  .company{font-size:16px;font-weight:300}
  .rule{height:1px;width:160px;margin:6px auto;background:linear-gradient(90deg,transparent,var(--rule),transparent)}
  .person{font-size:22px;font-weight:300;letter-spacing:-.02em}
  .role{font-size:12.5px;font-weight:300;letter-spacing:-.02em}
  .contact{position:absolute;left:8px;bottom:16px;list-style:none;font-size:11.5px;font-weight:300;line-height:19px}

  /* Horizontal card */
  .card-horizontal{left:622px;top:316px;width:434px;height:252px}
  .card-horizontal .band{position:absolute;left:130px;top:0;width:304px;height:202px;
        background:var(--walnut);border-bottom-left-radius:16px}
  .card-horizontal .panel{position:absolute;left:152px;top:0;width:282px;height:182px;
        background:var(--card);border-bottom-left-radius:14px}
  .card-horizontal .panel .brand{position:absolute;left:22px;top:58px}
</style>
</head>
<body>
  <div class="brand hero-brand">
    <span class="brand-dot"></span>
    <div class="brand-text">
      <span class="brand-name">VERUXO</span>
      <span class="brand-tagline">network security solutions</span>
    </div>
  </div>

  <section class="card card-vertical card-small" aria-label="Business card front">
    <div class="head">
      <div class="brand">
        <span class="brand-dot"></span>
        <div class="brand-text">
          <span class="brand-name">VERUXO</span>
          <span class="brand-tagline">network security solutions</span>
        </div>
      </div>
    </div>
    <div class="band"></div>
    <div class="panel">
      <div class="identity">
        <p class="company">Veruxo, LLC</p>
        <div class="rule"></div>
        <p class="person">Darren Colby</p>
        <p class="role">Principal Security Consultant</p>
        <div class="rule"></div>
      </div>
      <ul class="contact">
        <li>Mobile: +1-480-555-0137</li>
        <li>Email: Darren.Colby@Veruxo.example</li>
        <li>Web: www.veruxo.example</li>
      </ul>
    </div>
  </section>

  <section class="card card-horizontal card-small" aria-label="Business card back">
    <div class="band"></div>
    <div class="panel">
      <div class="brand">
        <span class="brand-dot"></span>
        <div class="brand-text">
          <span class="brand-name">VERUXO</span>
          <span class="brand-tagline">network security solutions</span>
        </div>
      </div>
    </div>
  </section>
</body>
</html>
```